Verlane Supply Chain and Logistic Consulting

Please review the attached Business Card. I want as close to this card with the colors, fonts, and quality of the card as possible. The attached compass should replace the deer head on both sides of the card and the text should say:

Backside
Compass JPEG
Verlane Group
A Supply Chain and Logistics Consulting Company

Frontside
Verlane Group
Ross Quillam - Harbor Vale Oregon
President
____________________________________
(555) 314-2960
VerlaneSCL@Mailbrook.com
_____________________________________

Bottom Front Side

Target Market(s)

Businesses

Contact Information for Business Card

Backside
Compass JPEG
Verlane Group

Frontside
Verlane Group
President
(555) 314-2960
VerlaneSCL@Mailbrook.com

Bottom Front Side

Font styles to use
Serif
Script

Colors

Designer to choose colors to be used in the design.

Requirements
Must have
• See attached card for reference
Nice to have
Should not have

```html
<!DOCTYPE html>
<html lang="en">
<head>
<meta charset="utf-8">
<title>Verlane Group Business Card</title>
<link rel="stylesheet" href="https://fonts.googleapis.com/css2?family=Cinzel:wght@400&display=swap">
<style>
  :root {
    --backdrop: #2a2b2e;
    --card: #0e0e10;
    --card-edge: #1b1b1e;
    --ink: #e9e6df;
    --ink-soft: #bdbab3;
    --rule: #8d8a84;
    --compass-deep: #2c4168;
    --compass-light: #6f86ad;
    --compass-steel: #8a97ab;
  }
  * { box-sizing: border-box; margin: 0; padding: 0; }
  html, body {
    width: 1200px; height: 900px; overflow: hidden;
    background: var(--backdrop);
  }
  .canvas {
    width: 1200px; height: 900px;
    display: flex; flex-direction: column;
    align-items: center; justify-content: center; gap: 40px;
    font-family: "Cinzel", "Times New Roman", serif;
    color: var(--ink);
  }
  .card {
    position: relative;
    width: 700px; height: 400px;
    background: var(--card);
    border: 1px solid var(--card-edge);
    overflow: hidden;
    display: flex; flex-direction: column; align-items: center;
    text-align: center;
  }

  /* Front side */
  .card-front { padding-top: 62px; }
  .faint-compass {
    position: absolute; left: 50%; top: 58%;
    width: 330px; height: 330px; transform: translate(-50%, -50%);
    border-radius: 50%;
    background: radial-gradient(circle, #1a1a1d 0%, #151518 55%, var(--card) 72%);
  }
  .front-content { position: relative; display: flex; flex-direction: column; align-items: center; }
  .company-name { font-size: 32px; letter-spacing: 2px; font-weight: 400; line-height: 1.2; }
  .person-line { margin-top: 10px; font-size: 19px; letter-spacing: 1px; }
  .person-role { margin-top: 6px; font-size: 14px; letter-spacing: 1px; color: var(--ink-soft); }
  .divider { width: 250px; height: 1px; background: var(--rule); margin: 14px 0; }
  .contact { font-size: 14px; letter-spacing: 1px; line-height: 1.75; color: var(--ink-soft); }
  .social-row { display: flex; align-items: center; gap: 8px; margin-top: 14px; }
  .social-row .rule-stub { width: 60px; height: 1px; background: var(--rule); }
  .social-tile { width: 18px; height: 18px; border: 1.5px solid var(--ink); border-radius: 2px; }
  .tagline-row {
    position: absolute; bottom: 34px; left: 40px; right: 40px;
    display: flex; align-items: center; gap: 14px;
  }
  .tagline-row .rule-line { flex: 1; height: 1px; background: var(--rule); }
  .tagline { font-size: 13px; letter-spacing: 1px; color: var(--ink-soft); white-space: nowrap; }

  /* Back side */
  .card-back { justify-content: center; }
  .compass-mark {
    width: 180px; height: 180px; border-radius: 50%;
    background: radial-gradient(circle, var(--compass-light) 0%, var(--compass-deep) 45%, var(--compass-steel) 70%, var(--card) 72%);
  }
  .back-name { margin-top: 18px; font-size: 32px; font-weight: 400; letter-spacing: 2px; line-height: 1.2; }
  .back-tagline { margin-top: 8px; font-size: 13px; letter-spacing: 1px; color: var(--ink-soft); }
</style>
</head>
<body>
<main class="canvas">
  <section class="card card-front">
    <div class="faint-compass" role="img" aria-label="Faint compass rose watermark"></div>
    <div class="front-content">
      <h1 class="company-name">Verlane Group</h1>
      <p class="person-line">Ross Quillam &bull; Harbor Vale Oregon</p>
      <p class="person-role">President</p>
      <div class="divider"></div>
      <p class="contact">(555) 314-2960<br>VerlaneSCL@Mailbrook.com</p>
      <div class="social-row">
        <span class="rule-stub"></span>
        <span class="social-tile"></span>
        <span class="social-tile"></span>
        <span class="social-tile"></span>
        <span class="rule-stub"></span>
      </div>
    </div>
    <div class="tagline-row">
      <span class="rule-line"></span>
      <p class="tagline">A Supply Chain and Logistics Consulting Company</p>
      <span class="rule-line"></span>
    </div>
  </section>

  <section class="card card-back">
    <div class="compass-mark" role="img" aria-label="Blue and steel compass rose with cardinal bearings"></div>
    <h2 class="back-name">Verlane Group</h2>
    <p class="back-tagline">A Supply Chain and Logistics Consulting Company</p>
  </section>
</main>
</body>
</html>
```